Varnok Development and Management Corp. Business Card

A logo design project has been started for our Calgary-Alberta, Canada based land development and project management company. Using this logo, a clean, sleek, professional business card is to be developed (for digital or print media) representing the principals of the company (community, sustainability, and harmony).
Updates

Project Deadline Extended
Reason: Logo design recently completed.

Adobe Illustrator Vector file uploaded. Thanks, Lew

Target Market(s)

Similar business development professionals and other engineering project management personnel involved in land developemtn. Also used to as as the brand and image with both private individuals (Landowners), public officials (policy makers), and investors (banks, venture capitalists).

Industry/Entity Type

Digital

Requirements
Must have
• Open to designers opinion. Based on logo. Must have logo, and space for employee name, title, address, website, office / cell numbers.
Should not have
• No Palm trees or tropical references. Company is based in Calgary, Alberta, Canada.

```html
<!DOCTYPE html>
<html lang="en">
<head>
<meta charset="utf-8">
<title>Varnok Development and Management Corp. Business Card</title>
<link href="https://fonts.googleapis.com/css2?family=Open+Sans:wght@400;600&display=swap" rel="stylesheet">
<style>
  :root {
    --backdrop: #e9e7e4;
    --card-dark: #2b2f39;
    --card-light: #ffffff;
    --brand-green: #9fbd35;
    --brand-grey: #7a7f87;
    --text-grey: #6a6e75;
    --text-white: #ffffff;
    --divider: #6e7279;
  }
  html, body {
    margin: 0;
    width: 1200px;
    height: 1000px;
    overflow: hidden;
    background: var(--backdrop);
    font-family: "Open Sans", Arial, sans-serif;
  }
  .canvas { position: relative; width: 1200px; height: 1000px; }
  .card {
    position: absolute;
    left: 265px;
    width: 665px;
    height: 397px;
    overflow: hidden;
  }
  .card--front { top: 73px; background: var(--card-dark); }
  .card--back { top: 533px; background: var(--card-light); }

  .front-brand {
    position: absolute;
    left: 262px;
    top: 150px;
    color: var(--text-white);
  }
  .front-brand__name {
    font-size: 52px;
    font-weight: 600;
    letter-spacing: 2px;
    line-height: 1;
    margin: 0;
  }
  .front-brand__tagline {
    font-size: 15px;
    margin: 8px 0 0 2px;
  }
  .front-brand__mark {
    position: absolute;
    left: -52px;
    top: 14px;
    width: 28px;
    height: 28px;
    background: var(--text-white);
  }

  .back-brand {
    position: absolute;
    left: 0;
    width: 333px;
    top: 170px;
    text-align: center;
  }
  .back-brand__name {
    font-size: 50px;
    font-weight: 600;
    letter-spacing: 2px;
    color: var(--brand-green);
    line-height: 1;
    margin: 0;
  }
  .back-brand__tagline {
    font-size: 14px;
    color: var(--brand-grey);
    margin: 8px 0 0;
  }
  .back-brand__mark {
    width: 34px;
    height: 34px;
    margin: 0 auto 20px;
    background: var(--brand-grey);
  }

  .divider {
    position: absolute;
    left: 333px;
    top: 97px;
    width: 2px;
    height: 208px;
    background: var(--divider);
  }

  .contact {
    position: absolute;
    left: 378px;
    top: 104px;
    color: var(--text-grey);
    font-size: 16px;
    line-height: 24px;
  }
  .contact__name {
    color: var(--brand-green);
    font-size: 20px;
    font-weight: 600;
    line-height: 24px;
    margin: 0;
  }
  .contact__title { margin: 0 0 22px; }
  .contact__address { margin: 0 0 6px; font-style: normal; }
  .contact__line {
    display: flex;
    align-items: center;
    gap: 6px;
    margin: 0 0 1px;
  }
  .contact__icon { width: 12px; height: 12px; flex: none; }

  .band { position: absolute; bottom: 0; left: 0; width: 665px; height: 24px; }
</style>
</head>
<body>
<div class="canvas">

  <section class="card card--front" aria-label="Card front">
    <div class="front-brand">
      <span class="front-brand__mark" aria-hidden="true"></span>
      <p class="front-brand__name">VARNOK</p>
      <p class="front-brand__tagline">Development and Management Corp</p>
    </div>
  </section>

  <section class="card card--back" aria-label="Card back">
    <div class="back-brand">
      <div class="back-brand__mark" aria-hidden="true"></div>
      <p class="back-brand__name">VARNOK</p>
      <p class="back-brand__tagline">Development and Management Corp</p>
    </div>

    <div class="divider"></div>

    <div class="contact">
      <p class="contact__name">Elias Brandt</p>
      <p class="contact__title">Director</p>
      <address class="contact__address">14 Harwick Lane<br>Calgary AB T2P 4K7</address>
      <p class="contact__line">
        <svg class="contact__icon" viewBox="0 0 12 12" aria-hidden="true">
          <rect x="3" y="0.5" width="6" height="11" rx="1" fill="none" stroke="#9fbd35" stroke-width="1.2"/>
          <rect x="5.2" y="9" width="1.6" height="1.2" fill="#9fbd35"/>
        </svg>
        +1 403 555 0192
      </p>
      <p class="contact__line">
        <svg class="contact__icon" viewBox="0 0 12 12" aria-hidden="true">
          <path d="M1 4 Q6 0 11 4 L9.5 5.5 L8 4.2 L4 4.2 L2.5 5.5 Z" fill="#9fbd35"/>
          <rect x="2.5" y="6" width="7" height="5" rx="1" fill="#9fbd35"/>
        </svg>
        +1 403 555 0148
      </p>
      <p class="contact__line">
        <svg class="contact__icon" viewBox="0 0 12 12" aria-hidden="true">
          <circle cx="6" cy="6" r="5" fill="none" stroke="#9fbd35" stroke-width="1.2"/>
          <ellipse cx="6" cy="6" rx="2.2" ry="5" fill="none" stroke="#9fbd35" stroke-width="1"/>
          <line x1="1" y1="6" x2="11" y2="6" stroke="#9fbd35" stroke-width="1"/>
        </svg>
        www.varnok.com
      </p>
    </div>

    <svg class="band" viewBox="0 0 665 24" aria-hidden="true">
      <polygon points="0,0 353,0 377,24 0,24" fill="var(--brand-green)"/>
      <polygon points="362,0 665,0 665,24 386,24" fill="var(--brand-grey)"/>
    </svg>
  </section>

</div>
</body>
</html>
```